QV - menu design

Hi,

We require elegant menu design for upscale restaurant. Please find attached the logo and the menu items for your reference.

for inspiration, this is a good website: -
http://www.platewhisper.example/bellfoldnotes/about.php

We are very much open for Menu Size suggestions.

unfortunately the place is going under renovation, we don't have updated images to it. the closest look and feel to our place is http://varnelo.example ..

we are also open for creative options on the shape, the styles, etc. as long as it represents the fine dine feel ...

Thanks ...

Dear All,

We wouldlike to extend our apology for not being able to provide feedbacks on everysingle design. We were extremely busy and we have multiple contests opensimultaneously which makes the process even harder.

However,we would like to thank you all for the efforts you have put into designingour menu. It is very much appreciated …

We wishyou all success in your design ventures and we are quite positive that we willbe working with many of you on many projects in the soon future. 

Thanks & Regards,

TLG Team...

 

 

 

Industry/Entity Type

Restaurant

Requirements
Must have
• Please ensure that there are 'some' images in the menu ... this is very important.
Should not have
• IMPORTANT: -

1. Please DO NOT insert any currency sign to the menu
2. Please keep the prices of the menu at the end of the menu items descriptions NOT beside the menu item names. The font of the price should be similar to the menu item description and please DO NOT bold the numbers. the prices should be subtle.

Thank you ...

```html
<!DOCTYPE html>
<html lang="en">
<head>
<meta charset="utf-8">
<title>QV – Menu</title>
<link rel="stylesheet" href="https://fonts.googleapis.com/css2?family=Cinzel:wght@400;700&family=Arimo:wght@400&family=Open+Sans:wght@400&family=Josefin+Sans:wght@300;400&display=swap">
<style>
  :root{
    --bg:#ece8e3;
    --paper:#ffffff;
    --cover-grey:#eeeeee;
    --accent:#8e1b1b;
    --ink:#222222;
    --rule:#9a7a6a;
    --shadow:rgba(0,0,0,.28);
  }
  *{margin:0;padding:0;box-sizing:border-box}
  html,body{width:1200px;height:660px;overflow:hidden;background:var(--bg)}
  .canvas{position:relative;width:1200px;height:660px}

  /* ---------- cover ---------- */
  .cover{position:absolute;left:25px;top:27px;width:373px;height:485px;background:var(--paper);box-shadow:3px 4px 10px var(--shadow)}
  .wood-band{height:28px;background:linear-gradient(90deg,#c9bca9,#d9cebf 30%,#c2b5a2 60%,#d4c8b8)}
  .cover-hero{height:203px;background:radial-gradient(circle at 25% 60%,#f2b25a 0%,#b23a1e 25%,#5a160e 60%,#2a0b07 100%)}
  .cover-brand{height:167px;background:var(--cover-grey);position:relative}
  .brand-mark{position:absolute;left:0;right:0;top:30px;text-align:center;font-family:"Josefin Sans",sans-serif;color:#333}
  .brand-mark .square{display:inline-block;width:10px;height:10px;background:#333;vertical-align:middle;margin-right:10px}
  .brand-mark .name{font-size:46px;font-weight:300;letter-spacing:10px;vertical-align:middle}
  .slogan{position:absolute;left:121px;top:127px;font-family:"Open Sans",sans-serif;font-size:15px;color:#222}
  .cover-strip{display:flex;gap:3px;height:87px}
  .cover-strip div{flex:1}

  /* ---------- inner spread ---------- */
  .spread{position:absolute;left:422px;top:117px;width:750px;height:483px;background:var(--paper);box-shadow:3px 4px 10px var(--shadow);font-family:"Arimo",sans-serif;color:var(--ink)}
  .spread .wood-band{height:30px}

  .section-title{position:absolute;font-family:"Cinzel",serif;font-weight:700;color:var(--accent);font-size:17px;line-height:22px;text-align:center;letter-spacing:.5px}
  .item{position:absolute;text-align:center}
  .item h3{font-family:"Cinzel",serif;font-weight:700;color:var(--accent);font-size:10.5px;line-height:14px}
  .item p{font-size:6.3px;line-height:7.6px;margin-top:2px}
  .divider{position:absolute;border-top:1px dotted var(--rule)}
  .sandwich{position:absolute;font-size:6.3px;line-height:7.6px}
  .sandwich p{margin-bottom:6px}

  .spread-strip{position:absolute;left:0;right:0;top:398px;height:85px;display:flex;gap:4px}
  .spread-strip div{flex:1}
</style>
</head>
<body>
<div class="canvas">

  <section class="cover">
    <div class="wood-band"></div>
    <div class="cover-hero" role="img" aria-label="Candlelit dinner table with wine glasses"></div>
    <div class="cover-brand">
      <div class="brand-mark"><span class="square"></span><span class="name">QV</span></div>
      <p class="slogan">Put Your Slogan Here</p>
    </div>
    <div class="cover-strip">
      <div role="img" aria-label="Breakfast spread with juice and tea" style="background:linear-gradient(135deg,#e9d6b8,#c98a4a)"></div>
      <div role="img" aria-label="Plate of eggs and bacon" style="background:linear-gradient(135deg,#f1e6d6,#c0573a)"></div>
      <div role="img" aria-label="Toast with honey" style="background:linear-gradient(135deg,#b5732f,#e3b26a)"></div>
    </div>
  </section>

  <section class="spread">
    <div class="wood-band"></div>

    <!-- breakfast -->
    <h2 class="section-title" style="left:13px;width:350px;top:37px">THE BREAKFAST</h2>
    <div class="item" style="left:13px;width:168px;top:64px"><h3>Butter Croissant</h3><p>Served plain with a selection of two jams, a vanilla custard cream, a chocolate Cream and butter curls. 36</p></div>
    <div class="item" style="left:13px;width:168px;top:103px"><h3>Cheese Croissant</h3><p>Crumbly freshly baked with cheese filling. 29</p></div>
    <div class="item" style="left:13px;width:168px;top:133px"><h3>Daily Fresh Eggs</h3><p>A choice of poached, scrambled, pan fried, omelet) all served with toasted Bread, mushrooms, roasted tomatoes and chicken sausages. 59</p></div>
    <div class="item" style="left:13px;width:168px;top:178px"><h3>Healthy Time</h3><p>One choice of hot beverage from our cafe served with fruit salad, natural Yoghurt, whole wheat bread vegetable sandwiches and sugar free biscuits selection.49</p></div>

    <div class="item" style="left:195px;width:168px;top:64px"><h3>Energy Time</h3><p>One choice of hot beverage from our cafe served with finger chocolate muffins, Poached egg with toasted bread and crispy beef bacon, crepe roll with goat Cheese and honey and finger chocolate cream with salted cookies. 59</p></div>
    <div class="item" style="left:195px;width:168px;top:125px"><h3>QV Time</h3><p>One choice of hot beverage from our cafe served with our selection of scones, Smoked salmon and avocado sandwich, roasted sausages sandwich, grilled vegetables sandwich, selection of our best biscuits. 59</p></div>
    <div class="item" style="left:195px;width:168px;top:177px"><h3>The Arabic Breakfast</h3><p>Choice of ZattarManakish and Cheese Manakish, served with one choice of hot beverage from our cafe and fresh orange juice. 59</p></div>

    <div class="divider" style="left:13px;width:350px;top:254px"></div>

    <!-- sandwiches -->
    <h2 class="section-title" style="left:13px;width:350px;top:277px;font-size:18px">THE SANDWICHES</h2>
    <div class="sandwich" style="left:28px;width:160px;top:316px">
      <p>Grilled Vegetables Sandwich with fresh Goat cheese and chives served with our Homemade spicy garlic mayo. 59</p>
      <p>Butterfish burger with fresh tomato, beef bacon, grilled vegetables and béarnaise sauce.</p>
      <p>Tataki Tuna sandwich with red onion slices, stewed endives and black olives andsultanas pate'. 79</p>
    </div>
    <div class="sandwich" style="left:208px;width:155px;top:316px">
      <p>Beef sirloin steak sandwich with grain mustard, Parmesan cheese and fresh Nashi pears. 79</p>
      <p>The Traditional Club sandwich served with French fries and vegetable chips. 69</p>
      <p>Chicken sandwich with Parmesan cheese slices, sundried tomatoes and mint Flavoredmayo. 69</p>
    </div>

    <!-- soup -->
    <h2 class="section-title" style="left:383px;width:358px;top:37px">SOUP</h2>
    <div class="item" style="left:383px;width:358px;top:64px"><h3>Bouillabaisse</h3><p>Traditional French Seafood soup, with Saffron and Estragon. 119</p></div>
    <div class="item" style="left:383px;width:358px;top:95px"><h3>Barley soup</h3><p>With fresh vegetables, tomato smoothie and a hint of garlic oil. 49</p></div>
    <div class="item" style="left:383px;width:358px;top:125px"><h3>Beef chili</h3><p>erved with Arabic bread, fresh guacamole and spicy black beans. 49</p></div>

    <div class="divider" style="left:383px;width:358px;top:182px"></div>

    <!-- salads -->
    <h2 class="section-title" style="left:383px;width:358px;top:208px;font-size:18px">SALADS</h2>
    <div class="item" style="left:393px;width:160px;top:233px"><h3>Vegetarian Salad</h3><p>Fresh green leaves, Italian cherry tomatoes, carrots, cucumber, green apple and toasted pine nuts with our special grain mustard dressing.59</p></div>
    <div class="item" style="left:393px;width:160px;top:278px"><h3>Sweet Gorgonzola<br>Cheese Salad</h3><p>Fresh green leaves, Gorgonzola cheese, fresh pears, walnuts, garlic bread croutons, green celery with smoked honey dressing.59</p></div>
    <div class="item" style="left:393px;width:160px;top:334px"><h3>Beef Sirloin Salad</h3><p>Fresh green leaves, beef sirloin julienne, caramelized apples, Parmesan cheese, toasted almonds, sundried tomatoes and light Pesto sauce.79</p></div>

    <div class="item" style="left:573px;width:160px;top:233px"><h3>Tandoori Chicken Salad</h3><p>Fresh green leaves, Tandoori chicken breast, fresh mango, fresh goat cheese, crispy chicken skin and Jasmine rice sauce.69</p></div>
    <div class="item" style="left:573px;width:160px;top:278px"><h3>Sea food Salad</h3><p>Fresh green leaves, fresh steamed seafood, black olives, celery, garlic bread croutons, avocado and grapefruit dressing.89</p></div>
    <div class="item" style="left:573px;width:160px;top:323px"><h3>Fresh Tuna Salad</h3><p>Fresh green leaves, low temperature cooked tuna, taggiasca olives, red onions, roasted peppers, soy marinated tofu and lemon dressing.89</p></div>

    <div class="spread-strip">
      <div role="img" aria-label="Breakfast table with juice and tea" style="background:linear-gradient(135deg,#efe2cc,#d39a55)"></div>
      <div role="img" aria-label="Club sandwich on a plate" style="background:linear-gradient(135deg,#6e8f3a,#d8b883)"></div>
      <div role="img" aria-label="Bowl of noodle soup with chopsticks" style="background:linear-gradient(135deg,#b22218,#e0a060)"></div>
      <div role="img" aria-label="Fresh green salad in a red bowl" style="background:linear-gradient(135deg,#4f8a2a,#c7352a)"></div>
    </div>
  </section>

</div>
</body>
</html>
```